Webbanner-Design holvira.at Webshop
Zielgruppe
Onlineshop für Haus + Garten
holvira.at
Aufgabenstellung
Benötigt wird ein neues Banner-Set
ein Allgemeines - warum bei holvira.at einkaufen
- günstige Preise durch Direktbezug ohne Zwischenhandel
- alle Artikel vorrätig - schnelle Lieferung
- Sichere Kaufabwicklung - Lumena Kauf
- Fachberatung und Service durch geschultes Peronal
sowie Banner für jede Hauptkategorie

```html
<!DOCTYPE html>
<html lang="de">
<head>
<meta charset="utf-8">
<title>holvira.at – Webshop</title>
<link rel="stylesheet" href="https://fonts.googleapis.com/css2?family=Open+Sans:wght@400;600;700&display=swap">
<style>
:root{
  --navy:#1d3f80;
  --blue:#2762a9;
  --gold:#c9a65f;
  --gold-text:#c49a45;
  --link:#2a7bbf;
  --text-grey:#555;
  --dark-btn:#3b3b3b;
  --white:#fff;
}
*{margin:0;padding:0;box-sizing:border-box}
html,body{width:1200px;height:745px;overflow:hidden;background:var(--white);font-family:"Open Sans",Arial,sans-serif}
.page{position:relative;width:1200px;height:745px}

.brand{position:absolute;left:56px;top:38px;display:flex;align-items:center;gap:8px}
.brand-square{width:22px;height:22px;background:var(--navy)}
.brand-name{font-size:26px;font-weight:700;color:var(--gold-text);letter-spacing:-0.5px}
.seal{position:absolute;left:342px;top:36px;width:52px;height:52px;border-radius:50%;background:var(--navy)}

.meta-links{position:absolute;left:892px;top:15px;font-size:12px;color:var(--link);display:flex}
.meta-links span{padding:0 7px;border-left:1px solid #ccc;line-height:16px}
.meta-links span:first-child{border-left:none;padding-left:0}
.lang{position:absolute;left:1069px;top:13px;width:77px;height:21px;background:var(--dark-btn);color:#fff;border-radius:3px;font-size:12px;line-height:21px;padding-left:8px}
.lang::after{content:"";position:absolute;right:7px;top:9px;border:4px solid transparent;border-top-color:#fff}

.search{position:absolute;left:676px;top:49px;width:242px;height:36px;border:1px solid #ccc;border-radius:3px;display:flex;overflow:hidden}
.search-input{flex:1;font-size:13px;color:#999;padding:9px 11px}
.search-btn{width:40px;background:#eee;border-left:1px solid #ccc;display:flex;align-items:center;justify-content:center}

.account,.cart{position:absolute;top:66px;font-size:14px;color:var(--link);display:flex;align-items:center;gap:4px}
.account{left:947px}.cart{left:1069px}
.caret{border:4px solid transparent;border-top-color:var(--link);margin-top:4px;margin-left:4px}

.navbar{position:absolute;left:0;top:110px;width:1200px;height:61px;background:linear-gradient(#fff,#ececec)}
.navbar ul{list-style:none;display:flex;position:absolute;top:20px;left:0;font-size:14px;color:var(--text-grey)}
.navbar li{position:absolute;white-space:nowrap}
.navbar li.drop::after{content:"";display:inline-block;border:4px solid transparent;border-top-color:var(--text-grey);margin-left:3px;vertical-align:-1px}

.backdrop{position:absolute;left:0;top:171px;width:1200px;height:574px;background:linear-gradient(90deg,#3f7f9a 0%,#a58a6a 4%,#c9dbe4 9%,#d7e5ec 50%,#c8dbe3 90%,#9a8c78 95%,#3a7c97 100%)}
.panel{position:absolute;left:50px;top:185px;width:1100px;height:550px;background:var(--white)}

.banner{position:absolute;left:73px;top:207px;width:1055px;height:439px;overflow:hidden;background:linear-gradient(160deg,var(--navy),var(--blue))}
.banner svg.scene{position:absolute;left:0;top:0}
.kicker{position:absolute;left:38px;top:34px;font-size:17px;color:#fff}
.kicker b{font-weight:700}
.headline{position:absolute;left:38px;top:80px;font-size:36px;font-weight:700;color:#fff;line-height:41px}
.features{position:absolute;left:38px;top:180px;list-style:none;font-size:22px;font-weight:700;color:#fff;line-height:28px}
.features li{display:flex;align-items:center;gap:6px}
.cta{position:absolute;left:38px;top:359px;width:155px;height:44px;background:var(--gold);color:#fff;font-size:12.5px;font-weight:700;text-align:center;line-height:44px}
.price-badge{position:absolute;left:889px;top:274px;width:128px;height:128px;border-radius:50%;background:var(--gold);color:#fff;text-align:center;font-weight:700}
.price-badge .label{font-size:11.5px;line-height:18px;margin-top:36px}
.price-badge .price{font-size:25px;line-height:30px}

.dots{position:absolute;left:520px;top:686px;display:flex;gap:18px;align-items:center}
.dots i{width:7px;height:7px;border-radius:50%;background:#444}
.dots i.active{width:10px;height:10px;background:#fff;border:2px solid #444}
</style>
</head>
<body>
<div class="page">
  <header>
    <div class="brand"><div class="brand-square"></div><div class="brand-name">holvira.at</div></div>
    <div class="seal"></div>
    <nav class="meta-links"><span>News</span><span>Kontakt</span><span>Links</span></nav>
    <div class="lang">Deutsch</div>
    <div class="search">
      <div class="search-input">Suchen</div>
      <div class="search-btn">
        <svg width="16" height="16" viewBox="0 0 16 16"><circle cx="6.5" cy="6.5" r="5" fill="none" stroke="#2a7bbf" stroke-width="2.2"/><line x1="10.2" y1="10.2" x2="14.5" y2="14.5" stroke="#2a7bbf" stroke-width="2.4" stroke-linecap="round"/></svg>
      </div>
    </div>
    <div class="account">
      <svg width="12" height="13" viewBox="0 0 12 13"><circle cx="6" cy="3.5" r="3.2" fill="#2a7bbf"/><path d="M0 13c0-4 2.5-6 6-6s6 2 6 6z" fill="#2a7bbf"/></svg>
      Anmelden<span class="caret"></span>
    </div>
    <div class="cart">
      <svg width="14" height="13" viewBox="0 0 14 13"><path d="M0 1h2.5l2 7h7.5l1.5-5H4" fill="none" stroke="#2a7bbf" stroke-width="1.8"/><circle cx="5.5" cy="11" r="1.4" fill="#2a7bbf"/><circle cx="11" cy="11" r="1.4" fill="#2a7bbf"/></svg>
      0,00 €<span class="caret"></span>
    </div>
  </header>

  <nav class="navbar">
    <ul>
      <li class="drop" style="left:64px">Badezimmer</li>
      <li class="drop" style="left:183px">Schwimmbecken</li>
      <li class="drop" style="left:328px">Schwimmbadzubehör</li>
      <li style="left:505px">Sauna</li>
      <li class="drop" style="left:572px">Heizung, Solar, Klima</li>
      <li class="drop" style="left:743px">Garten</li>
      <li style="left:826px">Kabelkanal</li>
      <li class="drop" style="left:923px">Whirlpoolzubehör</li>
    </ul>
  </nav>

  <div class="backdrop" role="img" aria-label="Unscharfes Hintergrundfoto in Blau- und Sandtönen"></div>
  <div class="panel"></div>

  <section class="banner">
    <svg class="scene" width="1055" height="439" viewBox="0 0 1055 439">
      <path d="M494 0 C410 80 380 330 479 439 H1055 V0 Z" fill="var(--gold)"/>
      <path d="M508 0 C430 90 405 320 494 439 H1055 V0 Z" fill="#8a8178" role="img" aria-label="Foto eines modernen Badezimmers mit freistehender Badewanne vor Natursteinwand"/>
      <defs><linearGradient id="room" x1="0" y1="0" x2="1" y2="1"><stop offset="0" stop-color="#6b6862"/><stop offset="0.55" stop-color="#b9b2a6"/><stop offset="1" stop-color="#4a3c33"/></linearGradient></defs>
      <path d="M508 0 C430 90 405 320 494 439 H1055 V0 Z" fill="url(#room)" opacity="0.85"/>
    </svg>
    <p class="kicker"><b>IHR FACHMANN</b> FÜR BAD, POOL UND MEHR</p>
    <h1 class="headline">ALLES FÜR IHR<br>BADEZIMMER</h1>
    <ul class="features">
      <li><svg width="16" height="18" viewBox="0 0 16 18"><path d="M1 0h6l8 9-8 9H1l8-9z" fill="var(--gold)"/></svg>BADEZIMMERMÖBEL</li>
      <li><svg width="16" height="18" viewBox="0 0 16 18"><path d="M1 0h6l8 9-8 9H1l8-9z" fill="var(--gold)"/></svg>DUSCHEN UND WANNEN</li>
      <li><svg width="16" height="18" viewBox="0 0 16 18"><path d="M1 0h6l8 9-8 9H1l8-9z" fill="var(--gold)"/></svg>ARMATUREN UVM.</li>
    </ul>
    <div class="cta">ENTDECKEN</div>
    <div class="price-badge">
      <div class="label">HOCHWERTIGES<br>ZUBEHÖR AB NUR</div>
      <div class="price">59,99€</div>
    </div>
  </section>

  <div class="dots"><i></i><i></i><i></i><i></i><i class="active"></i><i></i><i></i></div>
</div>
</body>
</html>
```